Exciting letterhead design for startup company

We need a A4 letterhead designing.

See attached file which contains the logo (on 3 different coloured backgrounds) and then the address and contact information. It also contains 4 colours that can be used.

Looking for an imaginative design. We are a young, fresh startup website design company so need a letterhead that reflects our industry.

Font styles to use
Sans Serif

```html
<!DOCTYPE html>
<html lang="en">
<head>
<meta charset="utf-8">
<title>PixelForge Letterhead</title>
<link href="https://fonts.googleapis.com/css2?family=Open+Sans:wght@400;600&display=swap" rel="stylesheet">
<style>
  :root {
    --ink: #222222;
    --brand-dark: #111111;
    --brand-light: #ffffff;
    --accent-blue: #3aa7d9;
    --accent-green: #6ab04c;
    --accent-orange: #efb32b;
    --paper: #ffffff;
  }
  html, body {
    margin: 0;
    padding: 0;
    overflow: hidden;
    background: var(--paper);
  }
  .letterhead {
    position: relative;
    width: 849px;
    height: 1200px;
    background: var(--paper);
    font-family: "Open Sans", Arial, sans-serif;
    color: var(--ink);
    overflow: hidden;
  }
  .brand-block {
    position: absolute;
    left: 51px;
    top: 23px;
    width: 246px;
    height: 85px;
    background: var(--brand-dark);
    display: flex;
    align-items: center;
    justify-content: center;
  }
  .brand-name {
    font-size: 40px;
    font-weight: 600;
    color: var(--brand-light);
    letter-spacing: -0.5px;
  }
  .contact-list {
    position: absolute;
    left: 542px;
    top: 38px;
    margin: 0;
    padding: 0;
    list-style: none;
    font-size: 14px;
    line-height: 19px;
  }
  .contact-item {
    display: flex;
    align-items: flex-start;
    margin-bottom: 3px;
  }
  .contact-icon {
    width: 14px;
    height: 14px;
    margin: 2px 8px 0 0;
    flex: none;
  }
  .footer-band {
    position: absolute;
    left: 0;
    bottom: 0;
    width: 100%;
    height: 38px;
    display: flex;
    font-size: 14px;
  }
  .footer-registration {
    width: 425px;
    background: var(--accent-green);
    display: flex;
    align-items: center;
    justify-content: flex-end;
    padding-right: 16px;
    box-sizing: border-box;
  }
  .footer-company {
    flex: 1;
    background: var(--accent-orange);
    display: flex;
    align-items: center;
    padding-left: 16px;
  }
</style>
</head>
<body>
<main class="letterhead">
  <header>
    <div class="brand-block">
      <span class="brand-name">PixelForge</span>
    </div>
    <ul class="contact-list">
      <li class="contact-item">
        <svg class="contact-icon" viewBox="0 0 14 14" aria-hidden="true">
          <path d="M2 3 Q7 0 12 3 L10.5 6 L8.5 5 L8.5 4 Q7 3.4 5.5 4 L5.5 5 L3.5 6 Z" fill="var(--accent-blue)"/>
          <rect x="3" y="7" width="8" height="5" rx="1" fill="var(--accent-blue)"/>
        </svg>
        <span>0845 000 1234</span>
      </li>
      <li class="contact-item">
        <svg class="contact-icon" viewBox="0 0 14 14" aria-hidden="true">
          <rect x="1" y="3" width="12" height="8" rx="1" fill="var(--accent-blue)"/>
          <path d="M1.5 3.5 L7 8 L12.5 3.5" fill="none" stroke="#ffffff" stroke-width="1"/>
        </svg>
        <span>hello@pixelforge.co.uk</span>
      </li>
      <li class="contact-item">
        <svg class="contact-icon" viewBox="0 0 14 14" aria-hidden="true">
          <path d="M7 13 C4 9 3 7 3 5.2 A4 4 0 0 1 11 5.2 C11 7 10 9 7 13 Z" fill="var(--accent-blue)"/>
          <circle cx="7" cy="5.2" r="1.6" fill="#ffffff"/>
        </svg>
        <span>PixelForge Limited, Suite 4,<br>Harbour Court, Leeds LS1 2AB</span>
      </li>
    </ul>
  </header>
  <footer class="footer-band">
    <div class="footer-registration">Registered in England &amp; Wales.</div>
    <div class="footer-company">Company No 01234567.</div>
  </footer>
</main>
</body>
</html>
```